Trade show flyer for award-winning, innovative folding helmet for cyclists

I am launching a brand new folding helmet for cyclists, skate boarders etc. It is being launched at a huge cycle show in Taiwan later this month and will be presented to special clients (corporates) who have been invited to view this stunning new product.
I have some pictures, a logo, a strap line and a little bit of copy that I would like to be included in the flyer.
I would like the flyer to be A4, colour both sides and probably folded once (to give 4 pages of A5)
The whole purpose of the flyer is to keep the helmet at the forefront of buyers minds when they return to their offices. This is a worlds first and an incredibly innovative, patented, trademarked product.
I need a glossy flyer that will appeal to cyclists and helmet manufacturers. The idea is to get big helmet brands to use our folding technology... almost (but not exactly) like an "vornik within" idea.
I have uploaded my logo and CG pictures of the product.
Updates

I will work on the copy and provide it ASAP. Certainly to any shortlisted designers. In the meantime, any text will do.

Also, I may decide to leave out the 2nd "we'll get you there" strap line.

                                       

I will add the text for the brochure  soon. Hopefully within 24 hours but quite possibly sooner.

Also, please forget about skate boarding etc as this is just for a bike show. So, for this project, just concentrate on the helmet being for cyclists.

The short time limit is because the show starts on March 20th and I have to have the flyers proofed, printed and delivered to Taipei by then!

Here is the text for the flyer: It's 159 words:

 

Quillet is an incredibly innovative new helmet which folds flat for easy portability! (Current helmets are awkward to carry and research shows this is why 91% of urban bike scheme users don't use one.)

Quillet looks stunning & is made to a superb standard by Harrowind Gear, the world's largest helmet manufacturer.
It's made in specialist EPS, Nylon & PC layers.

Patented worldwide, Quillet surpasses all relevant safety standards and its components are recyclable.
Quillet folds & unfolds quickly and simply so it's perfect for cyclists who want to carry a helmet more easily.

It's comfortable, convenient & safe!

Quillet is aimed at all urban cyclists. Eventually it will be marketed to all cyclists as well as other users of sports safety helmets (skiers, skaters, snow boarders, hockey players, horse riders etc)

Quillet has won major innovation awards in the UK and Europe.

Quillet’s flat profile will allow innovative selling methods such as at vending machines placed by major bicycle hire points.

Here is the Logo from Harrowind Gear, which should also appear on the flyer, as they are the manufacturers

The contact email address is info@quillethelmet.example and the website is www.quillethelmet.example

Thanks

Please note that there are a couple of minor changes to the copy as well as some other changes that I wish to make.

If you've already submitted a design then please DON'T resubmit it with the changes. That would be unnecessary work and we can address these small changes later if you win.

Please ensure that a small, raised "TM" is used every time Quillet is mentioned...

Also, please don't use the "Quillet... we'll get you there" strap line as I've gone off it.

Here is the new amended text:

 

Quillet looks stunning & is made to a superb standard by Harrowind Gear, the world's largest OEM helmet manufacturer.

Quillet is aimed at all cyclists. Eventually it will be marketed to other users of sports safety helmets such as skiers, skaters, snow boarders, hockey players, horse riders etc.

Target Market(s)

Senior management, Directors and owners of helmet brand companies

Industry/Entity Type

Trade

Requirements
Must have
• The logo, the pictures and the following text... Although some of this may be open to discussion...

Quillet... an open and shut case for the future of helmets.

Quillet... We'll get you there.

Winner Platinum Invention of the Year at the Grand Ideation Prizes
Winner "Transport Safety" award at Zentrix
Winner "Tamsel Lumora gold award" for Innovation

And copy, around 100 words, to be discussed.
Nice to have
• Design should somehow reflect innovation and safety, if possible....

```html
<!DOCTYPE html>
<html lang="en">
<head>
<meta charset="utf-8">
<title>Quillet folding helmet technology – flyer cover</title>
<link rel="stylesheet" href="https://fonts.googleapis.com/css2?family=Montserrat:wght@500;700;800&display=swap">
<style>
  :root {
    --ink-dark: #141414;
    --shadow-grey: #2b2b2b;
    --mid-grey: #4a4a4a;
    --helmet-red: #c0141a;
    --helmet-deep: #6e0608;
    --helmet-glow: #ff4a40;
    --paper: #ffffff;
    --brand-white: #ffffff;
    --maker-blue: #1c4fa0;
  }
  * { margin: 0; padding: 0; box-sizing: border-box; }
  html, body {
    width: 849px;
    height: 1200px;
    overflow: hidden;
    background: var(--paper);
  }
  .flyer-cover {
    position: relative;
    width: 849px;
    height: 1200px;
    overflow: hidden;
    background: var(--paper);
    font-family: "Montserrat", Arial, sans-serif;
  }
  .product-render {
    position: absolute;
    left: 0;
    top: 0;
    width: 849px;
    height: 1090px;
    background:
      radial-gradient(ellipse 420px 330px at 330px 360px, var(--helmet-glow) 0%, var(--helmet-red) 35%, var(--helmet-deep) 75%, transparent 100%),
      radial-gradient(ellipse 520px 260px at 360px 760px, var(--helmet-red) 0%, var(--helmet-deep) 60%, transparent 100%),
      radial-gradient(ellipse 160px 420px at 770px 820px, #d8d8d8 0%, #8a8a8a 40%, transparent 100%),
      linear-gradient(160deg, var(--mid-grey) 0%, var(--shadow-grey) 45%, var(--ink-dark) 100%);
  }
  .brand-lockup {
    position: absolute;
    right: 40px;
    top: 92px;
    width: 280px;
    text-align: center;
    color: var(--brand-white);
  }
  .brand-name {
    display: block;
    font-size: 62px;
    font-weight: 800;
    letter-spacing: 2px;
    line-height: 1;
    text-transform: uppercase;
  }
  .brand-tagline {
    display: block;
    margin-top: 14px;
    font-size: 27px;
    font-weight: 500;
    letter-spacing: 0.2px;
    line-height: 1;
  }
  .maker-lockup {
    position: absolute;
    right: 18px;
    top: 1108px;
    display: flex;
    align-items: center;
    gap: 12px;
  }
  .maker-mark {
    width: 40px;
    height: 40px;
    background: var(--maker-blue);
  }
  .maker-text {
    color: var(--maker-blue);
    font-weight: 700;
  }
  .maker-name {
    display: block;
    font-size: 27px;
    line-height: 1.05;
    text-transform: uppercase;
    letter-spacing: 0.5px;
  }
  .maker-motto {
    display: block;
    font-size: 18px;
    line-height: 1.2;
    text-align: right;
  }
</style>
</head>
<body>
  <main class="flyer-cover">
    <div class="product-render" role="img" aria-label="Close-up render of the glossy red folding helmet with vented segmented shell, resting on a dark grey tyre-tread background"></div>

    <header class="brand-lockup">
      <span class="brand-name">Quillet</span>
      <span class="brand-tagline">folding helmet technology</span>
    </header>

    <footer class="maker-lockup">
      <span class="maker-mark" aria-hidden="true"></span>
      <div class="maker-text">
        <span class="maker-name">Harrowind Gear Ltd</span>
        <span class="maker-motto">Protecting Life</span>
      </div>
    </footer>
  </main>
</body>
</html>
```